Group training gym/bootcamp needs a web design

We need a website for our gym that is based in Sydney. We have indoor functional training classes and outdoor bootcamp classes. We would like the web site to have a video (to be created) and photo gallery. I would like the site made on word press and i would like to be able to make minor changes such as changing images and text without having to use a designer.

The website should have the following pages: home page; the gym; the bootcamp; photo gallery; about us; contact.

I have uploaded our logo and i would like to keep to these colour (blue,yellow,silver) and black is also allowed

Target Market(s)

18-50 male and female

Industry/Entity Type

Gym

Coding

Coded - Design and coding required

Number of Pages Required

5+ page

Font styles to use
Sans Serif

Colors
0692cd
fbed22
1b1b1b
e8e8e8

Requirements
Must have
• The website should have the following pages: home page; the gym; the bootcamp; photo gallery; about us; contact.
• I have uploaded our logo and i would like to keep to these colour (blue,yellow,silver) and black is also allowed
• Video upload and photo upload

```html
<!DOCTYPE html>
<html lang="en">
<head>
<meta charset="utf-8">
<title>The Bootcamp – Ironline Training Hub</title>
<link href="https://fonts.googleapis.com/css2?family=Oswald:wght@500;600;700&family=Open+Sans:wght@400&family=Roboto:wght@300;500&family=Lato:wght@300;700&display=swap" rel="stylesheet">
<style>
  :root{
    --blue:#2e86c8;
    --blue-btn:#2f8ad0;
    --yellow:#f2c418;
    --orange:#f05a1a;
    --ink:#1b1b1b;
    --text:#6b6b6b;
    --silver:#e8e8e8;
    --white:#ffffff;
    --header-a:#1a2a3d;
    --header-b:#0f1a28;
  }
  *{margin:0;padding:0;box-sizing:border-box}
  html,body{width:797px;height:1200px;overflow:hidden;background:var(--white)}
  .page{position:relative;width:797px;height:1200px;overflow:hidden;font-family:"Open Sans",sans-serif}

  .site-header{position:absolute;left:0;top:0;width:797px;height:142px;
    background:radial-gradient(ellipse at 50% 40%,#2a3b52 0%,var(--header-a) 45%,var(--header-b) 100%)}
  .brand{position:absolute;left:0;top:40px;width:797px;text-align:center;
    font-family:"Oswald",sans-serif;font-weight:600;font-size:14px;letter-spacing:.5px;color:var(--yellow)}
  .brand-dot{display:inline-block;width:10px;height:10px;border-radius:50%;background:var(--blue);margin-right:6px;vertical-align:1px}
  .main-nav{position:absolute;top:85px;left:0;width:797px;display:flex;justify-content:center;gap:18px}
  .main-nav a{font-family:"Oswald",sans-serif;font-weight:500;font-size:9.5px;color:var(--white);text-decoration:none;letter-spacing:.2px}
  .main-nav a.is-active{color:var(--yellow)}

  .page-title{position:absolute;left:123px;top:166px;font-family:"Oswald",sans-serif;font-weight:700;
    font-size:41px;line-height:1;color:var(--blue);letter-spacing:-.3px}
  .intro{position:absolute;left:124px;top:227px;width:550px;font-size:7.4px;line-height:12px;color:var(--text)}
  .intro p+p{margin-top:12px}

  .class-grid{position:absolute;left:124px;top:350px;width:549px;display:grid;
    grid-template-columns:repeat(3,173px);column-gap:15px;row-gap:38px}
  .class-card{position:relative;height:144px}
  .class-photo{width:173px;height:144px}
  .class-label{position:absolute;left:15px;bottom:-19px;width:142px;height:26px;border-radius:13px;
    background:var(--white);box-shadow:0 2px 3px rgba(0,0,0,.08);
    font-family:"Roboto",sans-serif;font-weight:500;font-size:9px;color:var(--orange);
    display:flex;align-items:center;justify-content:center}

  .pager{position:absolute;left:367px;top:720px;display:flex;gap:1px}
  .pager span{width:19px;height:17px;display:flex;align-items:center;justify-content:center;
    font-family:"Roboto",sans-serif;font-size:7.5px;color:var(--white);background:#b9b9b9}
  .pager span.is-current{background:var(--yellow)}

  .promo{position:absolute;left:0;top:772px;width:797px;height:272px;
    background:linear-gradient(90deg,#4a4f55 0%,#33373c 30%,#1e1f21 55%,#161616 100%)}
  .promo-copy{position:absolute;left:282px;top:60px;color:var(--white);font-family:"Lato",sans-serif}
  .promo-title{font-weight:700;font-size:24px;letter-spacing:.3px;line-height:1}
  .promo-offer{margin-top:12px;font-weight:300;font-size:24px;line-height:29px;letter-spacing:.3px}
  .promo-offer em{font-style:normal;color:var(--yellow)}
  .btn-member{position:absolute;left:280px;top:167px;width:118px;height:30px;border-radius:15px;
    background:var(--blue-btn);color:var(--white);font-family:"Oswald",sans-serif;font-weight:500;
    font-size:11.5px;display:flex;align-items:center;justify-content:center;text-decoration:none}

  .site-footer{position:absolute;left:0;top:1044px;width:797px;height:156px}
  .footer-brand{position:absolute;top:56px;width:797px;text-align:center;
    font-family:"Oswald",sans-serif;font-weight:600;font-size:13px;color:var(--yellow)}
  .social{position:absolute;top:91px;left:358px;display:flex;gap:8px}
  .social span{width:14px;height:14px;border:1px solid #333;border-radius:50%}
  .copyright{position:absolute;top:115px;width:797px;text-align:center;font-family:"Roboto",sans-serif;
    font-weight:300;font-size:8.5px;color:var(--text)}
  .footer-bar{position:absolute;left:0;bottom:0;width:797px;height:7px;background:var(--blue)}
  .footer-notch{position:absolute;left:373px;bottom:6px}
</style>
</head>
<body>
<div class="page">
  <header class="site-header" role="img" aria-label="Dark blue photo of an athlete holding dumbbells">
    <div class="brand"><span class="brand-dot"></span>IRONLINE TRAINING HUB</div>
    <nav class="main-nav">
      <a href="#">HOME</a>
      <a href="#">THE GYM</a>
      <a href="#" class="is-active">THE BOOTCAMP</a>
      <a href="#">PHOTO GALLERY</a>
      <a href="#">ABOUT US</a>
      <a href="#">CONTACT</a>
    </nav>
  </header>

  <h1 class="page-title">THE BOOTCAMP</h1>
  <div class="intro">
    <p>Quisque et lectus pulvinar, porttitor mi non, elementum dui. Morbi mi nisl, tincidunt sed venenatis eget, finibus eu mauris. Nullam nisi lacus, feugiat eget varegeellentesque dictum odio. Sed sollicitudin viverra est, at aliquam metus ultrices id. Duis eu purus vel nisl commodo facilisis vitae ut lectus. Sed elementum dapibus tellus, a dictum metus interdum ac. Nullam condimentum, dui volutpat fringilla molestie, libero tortor ultrices lorem, at tempus diam purus non velit. Aliquam vel nulla eleifend, consequat elit id, tristique massa. Fusce dolor velit, blandit ac erat ac, vestibulum ornare diam.</p>
    <p>Sed sollicitudin viverra est, at aliquam metu eratys ultrices tristique massaid.diam purus non velit. Aliquam vel nulla eleifend, consequat elit id, tristique massa. Fusce dolor velit, blandit ac erat ac, vestibulum ornare diam. Sed sollicitudin viverra.</p>
  </div>

  <section class="class-grid">
    <div class="class-card"><div class="class-photo" role="img" aria-label="Woman lifting dumbbells overhead in a gym" style="background:linear-gradient(135deg,#dfe6ec,#8c8f94 60%,#2a2a2a)"></div><div class="class-label">Cycling</div></div>
    <div class="class-card"><div class="class-photo" role="img" aria-label="Trainer assisting a man with a dumbbell press" style="background:linear-gradient(135deg,#b8b8b4,#6e6660 55%,#2b2522)"></div><div class="class-label">Martial Arts</div></div>
    <div class="class-card"><div class="class-photo" role="img" aria-label="Woman doing a dumbbell press on a bench" style="background:linear-gradient(135deg,#7a2a30,#c98f7c 55%,#e9d2c4)"></div><div class="class-label">Running</div></div>
    <div class="class-card"><div class="class-photo" role="img" aria-label="Group class doing dumbbell rows with step platforms" style="background:linear-gradient(160deg,#9aa0ab,#8a5d5a 60%,#6e4040)"></div><div class="class-label">Meditation</div></div>
    <div class="class-card"><div class="class-photo" role="img" aria-label="Women training with kettlebells in a bright gym" style="background:linear-gradient(160deg,#d9e4ea,#9fb2ba 55%,#6f8a8a)"></div><div class="class-label">Karate</div></div>
    <div class="class-card"><div class="class-photo" role="img" aria-label="Trainer assisting a man with a dumbbell press" style="background:linear-gradient(135deg,#b8b8b4,#6e6660 55%,#2b2522)"></div><div class="class-label">Yoga</div></div>
  </section>

  <div class="pager"><span class="is-current">1</span><span>2</span><span>»</span></div>

  <section class="promo" role="img" aria-label="Runner's legs on a treadmill in dim light">
    <div class="promo-copy">
      <div class="promo-title">FITNESS CLASSES THIS SUMMER</div>
      <div class="promo-offer">PAY NOW AND<br><em>GET 35%</em> DISCOUNT</div>
    </div>
    <a href="#" class="btn-member">BECOME A MEMBER</a>
  </section>

  <footer class="site-footer">
    <div class="footer-brand"><span class="brand-dot"></span>IRONLINE TRAINING HUB</div>
    <div class="social"><span></span><span></span><span></span><span></span></div>
    <div class="copyright">Copyright © Ironline Training Hub 2017. All Rights Reserved | Privacy Policy | Terms of Use</div>
    <svg class="footer-notch" width="50" height="16" viewBox="0 0 50 16"><polygon points="0,16 25,0 50,16" fill="#2e86c8"/></svg>
    <div class="footer-bar"></div>
  </footer>
</div>
</body>
</html>
```